Bref créative
see logo info from logo info
Bluefern Trading Partners, Ltd.
Use same font as used in my logo
can also give other font suggestions
Modern
Daniel Okafor
President
742 Hollis St. - Suite 0830
New York, NY 10093
212-555-0147 Ext-305
sales@bluefernexample.com
bluefernexample.com
we are looking for business card and stationary design layouts.
logo with name
This is our logo to be used for the layout of the business cards and stationary.

```html
<!DOCTYPE html>
<html lang="en">
<head>
<meta charset="utf-8">
<title>Bluefern Trading Partners – Business Cards</title>
<link href="https://fonts.googleapis.com/css2?family=Cinzel:wght@400;700&family=Open+Sans:wght@400;600&display=swap" rel="stylesheet">
<style>
  :root {
    --blue: #1f5fb8;
    --blue-deep: #17479a;
    --navy: #0f2c66;
    --white: #ffffff;
    --paper: #f4f5f7;
    --grey: #8a8f99;
    --ink: #1c3f85;
    --stage: #e6e8ec;
  }
  * { margin: 0; padding: 0; box-sizing: border-box; }
  html, body { width: 1200px; height: 864px; overflow: hidden; }
  body {
    background: var(--stage);
    display: flex;
    align-items: center;
    justify-content: center;
    gap: 40px;
    font-family: "Open Sans", sans-serif;
  }
  .card {
    position: relative;
    width: 540px;
    height: 309px;
    border-radius: 16px;
    overflow: hidden;
    box-shadow: 0 10px 30px rgba(0,0,0,.18);
  }
  /* Back */
  .card-back {
    background: radial-gradient(circle at 50% 40%, var(--blue) 0%, var(--blue-deep) 100%);
    display: flex;
    flex-direction: column;
    align-items: center;
    justify-content: center;
    color: var(--white);
  }
  .brand-mark {
    width: 58px; height: 58px;
    border-radius: 50%;
    border: 3px solid var(--white);
    margin-bottom: 14px;
  }
  .brand-name-back {
    font-family: "Cinzel", serif;
    font-weight: 700;
    font-size: 20px;
    letter-spacing: 1px;
    color: var(--white);
  }
  .website-back {
    margin-top: 10px;
    font-family: "Cinzel", serif;
    font-size: 10px;
    letter-spacing: 2px;
    text-transform: uppercase;
    opacity: .9;
  }
  /* Front */
  .card-front { background: linear-gradient(135deg, var(--white) 0%, var(--paper) 100%); }
  .front-curve { position: absolute; inset: 0; width: 100%; height: 100%; }
  .identity {
    position: absolute;
    left: 34px; top: 70px;
    width: 260px;
  }
  .brand-lockup { display: flex; align-items: center; gap: 10px; }
  .brand-mark-small {
    width: 34px; height: 34px; border-radius: 50%;
    background: var(--blue); flex: none;
  }
  .brand-name-front {
    font-family: "Cinzel", serif;
    font-weight: 700;
    font-size: 17px;
    line-height: 1.15;
    color: var(--ink);
  }
  .rule { height: 1px; background: var(--grey); margin: 14px 0 12px; width: 230px; }
  .person-name {
    font-family: "Cinzel", serif;
    font-size: 13px;
    color: var(--blue);
    letter-spacing: .5px;
  }
  .person-title {
    font-family: "Cinzel", serif;
    font-size: 9px;
    color: var(--grey);
    letter-spacing: 1px;
    margin-bottom: 10px;
  }
  .address {
    font-family: "Cinzel", serif;
    font-size: 10px;
    line-height: 1.6;
    color: var(--grey);
    font-style: normal;
  }
  .contact-list {
    position: absolute;
    left: 368px; top: 88px;
    list-style: none;
    color: var(--white);
    font-size: 9.5px;
    white-space: nowrap;
  }
  .contact-list li { display: flex; align-items: center; gap: 6px; margin-bottom: 9px; }
  .contact-icon {
    width: 15px; height: 15px; border-radius: 50%;
    background: var(--white); flex: none;
  }
</style>
</head>
<body>
  <section class="card card-back" aria-label="Business card back">
    <div class="brand-mark"></div>
    <div class="brand-name-back">Bluefern Trading Partners, Ltd.</div>
    <div class="website-back">www.bluefernexample.com</div>
  </section>

  <section class="card card-front" aria-label="Business card front">
    <svg class="front-curve" viewBox="0 0 540 309" preserveAspectRatio="none" aria-hidden="true">
      <path d="M305 0 C 345 90, 340 210, 275 309 L540 309 L540 0 Z" fill="var(--navy)"/>
      <path d="M316 0 C 356 90, 351 210, 286 309 L540 309 L540 0 Z" fill="var(--white)"/>
      <path d="M323 0 C 363 90, 358 210, 294 309 L540 309 L540 0 Z" fill="var(--blue)"/>
    </svg>

    <div class="identity">
      <div class="brand-lockup">
        <div class="brand-mark-small"></div>
        <div class="brand-name-front">BLUEFERN TRADING<br>PARTNERS, LTD.</div>
      </div>
      <div class="rule"></div>
      <div class="person-name">DANIEL OKAFOR</div>
      <div class="person-title">PRESIDENT</div>
      <address class="address">742 HOLLIS ST. - SUITE 0830<br>NEW YORK, NY 10093</address>
    </div>

    <ul class="contact-list">
      <li>
        <svg class="contact-icon" viewBox="0 0 16 16"><circle cx="8" cy="8" r="8" fill="#fff"/><path d="M5 4.5l1.5-.5 1 2-1 .8a5 5 0 0 0 2.2 2.2l.8-1 2 1-.5 1.5c-3.5 0-6-2.5-6-6z" fill="var(--blue)"/></svg>
        212-555-0147 Ext-305
      </li>
      <li>
        <svg class="contact-icon" viewBox="0 0 16 16"><circle cx="8" cy="8" r="8" fill="#fff"/><rect x="4.5" y="6" width="7" height="5" fill="var(--blue)"/><rect x="6" y="4" width="4" height="2.5" fill="var(--blue)"/></svg>
        212-555-0162
      </li>
      <li>
        <svg class="contact-icon" viewBox="0 0 16 16"><circle cx="8" cy="8" r="8" fill="#fff"/><rect x="4" y="5.5" width="8" height="5.5" fill="none" stroke="var(--blue)"/><path d="M4 5.5l4 3 4-3" fill="none" stroke="var(--blue)"/></svg>
        sales@bluefernexample.com
      </li>
      <li>
        <span class="contact-icon"></span>
        Bluefern_Trading
      </li>
      <li>
        <svg class="contact-icon" viewBox="0 0 16 16"><circle cx="8" cy="8" r="8" fill="#fff"/><circle cx="8" cy="8" r="4" fill="none" stroke="var(--blue)"/><path d="M4 8h8M8 4v8" stroke="var(--blue)"/></svg>
        www.bluefernexample.com
      </li>
    </ul>
  </section>
</body>
</html>
```